Business Card Design Project

Use our current logo. Clean design.

Industry/Entity Type

Business

Requirements
Must have
• Marisela DUBRANCQ
M. Law
Managing Partner

Alpenvorsa AG
Kornhalmweg 214
CH-3097 Liebefeld

M. +41 79 412 56 27
T. +41 31 928 44 10
F. +41 31 928 44 19

m.dubrancq@alpenvorsa-example.com
www.alpenvorsa-example.com

```html
<!DOCTYPE html>
<html lang="en">
<head>
<meta charset="utf-8">
<title>Alpenvorsa AG – Business Card</title>
<link rel="stylesheet" href="https://fonts.googleapis.com/css2?family=Lato:wght@400;700&family=Tenor+Sans&family=Marcellus&display=swap">
<style>
  :root {
    --ink: #111111;
    --paper: #ffffff;
    --card-black: #000000;
    --rule: #555555;
    --border: #8a8a8a;
    --brand-red: #e3161b;
  }
  * { box-sizing: border-box; margin: 0; padding: 0; }
  html, body { width: 1200px; height: 848px; overflow: hidden; background: var(--paper); }
  body { position: relative; font-family: "Lato", Arial, sans-serif; color: var(--ink); }

  .card { position: absolute; width: 364px; }
  .card-front { left: 39px; top: 259px; height: 221px; background: var(--card-black); color: var(--paper); }
  .card-back { left: 39px; top: 509px; height: 222px; background: var(--paper); border: 1px solid var(--border); }

  .front-brand-line {
    position: absolute; left: 26px; top: 3px;
    font-family: "Tenor Sans", "Lato", sans-serif; font-size: 14px; letter-spacing: 0.2px;
  }
  .front-brand-name {
    position: absolute; left: 52px; top: 160px;
    font-family: "Marcellus", Georgia, serif; font-size: 40px; line-height: 1;
  }

  .rule { position: absolute; left: 21px; width: 321px; height: 1px; background: var(--rule); }
  .rule-top { top: 49px; }
  .rule-bottom { top: 170px; }

  .person { position: absolute; left: 21px; top: 55px; font-size: 11.5px; line-height: 15px; }
  .person-name { font-weight: 700; font-size: 12px; }

  .contacts { position: absolute; left: 21px; top: 117px; list-style: none; font-size: 9px; line-height: 12px; }
  .contacts li { display: flex; align-items: center; }
  .contact-label { width: 11px; font-weight: 700; }
  .plus-box { width: 8px; height: 8px; margin-right: 3px; }

  .website {
    position: absolute; left: 21px; top: 175px;
    font-size: 10.5px; font-weight: 700; color: var(--brand-red);
  }

  .company-mark { position: absolute; left: 258px; top: 58px; display: flex; align-items: center; gap: 5px; }
  .mark-square { width: 20px; height: 20px; background: var(--brand-red); }
  .mark-name { font-size: 12px; font-weight: 700; color: var(--brand-red); }

  .address { position: absolute; left: 258px; top: 129px; font-style: normal; font-size: 9px; line-height: 12.5px; }
</style>
</head>
<body>
  <section class="card card-front" aria-label="Card front">
    <p class="front-brand-line">ALPENVORSA</p>
    <p class="front-brand-name">Alpenvorsa</p>
  </section>

  <section class="card card-back" aria-label="Card back">
    <div class="rule rule-top"></div>

    <div class="person">
      <p class="person-name">Marisela DUBRANCQ</p>
      <p>M. Law</p>
      <p>Managing Partner</p>
    </div>

    <div class="company-mark">
      <span class="mark-square"></span>
      <span class="mark-name">Alpenvorsa</span>
    </div>

    <ul class="contacts">
      <li><span class="contact-label">M</span><svg class="plus-box" viewBox="0 0 8 8"><rect width="8" height="8" fill="#111"/><path d="M4 1.8v4.4M1.8 4h4.4" stroke="#fff" stroke-width="1"/></svg>41 79 412 56 27</li>
      <li><span class="contact-label">T</span><svg class="plus-box" viewBox="0 0 8 8"><rect width="8" height="8" fill="#111"/><path d="M4 1.8v4.4M1.8 4h4.4" stroke="#fff" stroke-width="1"/></svg>41 31 928 44 10</li>
      <li><span class="contact-label">F</span><svg class="plus-box" viewBox="0 0 8 8"><rect width="8" height="8" fill="#111"/><path d="M4 1.8v4.4M1.8 4h4.4" stroke="#fff" stroke-width="1"/></svg>41 31 928 44 19</li>
      <li><span class="contact-label">E</span>m.dubrancq@alpenvorsa-example.com</li>
    </ul>

    <address class="address">
      Alpenvorsa AG<br>
      Kornhalmweg 214,<br>
      CH-3097 Liebefeld
    </address>

    <div class="rule rule-bottom"></div>
    <p class="website">www.alpenvorsa-example.com</p>
  </section>
</body>
</html>
```